Property Investment eBook Cover

I am a long established Australian property investment adviser, analyst and consultant who is now in semi-retired mode and have re-branded to reflect a more casual and personal approach to advising my property investor clients. I am writing a 'revised edition' to a book written in partnership with my father 20 years ago and need an eBook Cover for this new edition. The eBook will be uploaded to all the regular Australian providers (Larkfield Reader, Quince Folio, Tavi, Pagemarten)

The 3 key elements in the book cover are:

Title: The Harvest Engine of Land. The word 'Property' should be larger and more prominent. eg "The Wealth Power of" could be 1/3 the size of "Property" - with both justified left

Edition: Sydney 2021. "Sydney 2021" should be the focus and dominant imagery of the eBook cover and more prominent than the Title or Author

Author: Colin Marsh, The Housing Ledger Guide. The word "Author" should not appear. "The Housing Ledger Guide" should appear underneath Colin Marsh and justified to Colin Marsh, therefore a smaller font.

The cover should be simple, but eye-catching. No property images, more of an abstract background, than a background with an image. Our preferred colour palette is more blues/greens. Prefer SerifFonts

Copy of book published 20 years ago attached for reference only

```html
<!DOCTYPE html>
<html lang="en">
<head>
<meta charset="utf-8">
<title>The Harvest Engine of Land – Sydney 2021</title>
<link rel="stylesheet" href="https://fonts.googleapis.com/css2?family=Oswald:wght@600&family=Cinzel:wght@400;600;700&display=swap">
<style>
  :root {
    --gold-light: #f3d248;
    --gold-mid: #e3b52a;
    --gold-dark: #c8901a;
    --title-red: #a8401c;
    --blue: #2e59a8;
    --blue-deep: #234a93;
    --blue-tear: #3a64b0;
    --white: #ffffff;
    --tag-yellow: #f5e21c;
  }
  html, body {
    margin: 0;
    padding: 0;
    width: 750px;
    height: 1200px;
    overflow: hidden;
    background: var(--blue);
  }
  .cover {
    position: relative;
    width: 750px;
    height: 1200px;
    overflow: hidden;
    background: linear-gradient(180deg, var(--blue) 0%, var(--blue-deep) 100%);
  }
  .cover__gold {
    position: absolute;
    left: 0; top: 0;
    width: 750px; height: 470px;
    background: radial-gradient(ellipse at 50% 20%, var(--gold-light) 0%, var(--gold-mid) 55%, var(--gold-dark) 100%);
  }
  .cover__tear {
    position: absolute;
    left: 0; top: 390px;
    width: 750px; height: 100px;
  }
  .title {
    position: absolute;
    left: 0; top: 0;
    width: 750px;
    height: 380px;
    margin: 0;
  }
  .title text {
    font-family: "Oswald", sans-serif;
    font-weight: 600;
    fill: var(--title-red);
    text-transform: uppercase;
  }
  .rule {
    position: absolute;
    left: 0;
    width: 750px;
    height: 8px;
    background: var(--white);
  }
  .rule--top { top: 516px; }
  .rule--bottom { top: 958px; }
  .edition {
    position: absolute;
    left: 0; top: 530px;
    width: 750px;
    height: 420px;
  }
  .edition text {
    font-family: "Cinzel", serif;
    font-weight: 700;
    fill: var(--white);
  }
  .author {
    position: absolute;
    left: 0; top: 1020px;
    width: 750px;
    height: 140px;
  }
  .author text {
    font-family: "Cinzel", serif;
  }
  .author__name { fill: var(--white); font-weight: 400; }
  .author__tag { fill: var(--tag-yellow); font-weight: 600; }
</style>
</head>
<body>
<main class="cover">
  <div class="cover__gold"></div>

  <svg class="cover__tear" viewBox="0 0 750 100" aria-hidden="true">
    <path fill="var(--blue-tear)" d="M0 32 L30 28 L58 34 L90 26 L120 30 L150 24 L185 31 L215 25 L250 34 L280 27 L312 35 L345 20 L378 28 L410 22 L440 30 L470 18 L505 26 L540 20 L572 28 L600 21 L632 29 L665 23 L700 30 L730 24 L750 27 L750 100 L0 100 Z"/>
    <path fill="var(--blue)" d="M0 44 L28 40 L60 47 L95 39 L125 44 L160 37 L190 45 L222 39 L255 48 L288 41 L318 49 L350 34 L382 42 L415 36 L445 44 L478 32 L510 40 L545 34 L578 42 L606 35 L640 43 L672 37 L705 44 L735 38 L750 41 L750 100 L0 100 Z"/>
  </svg>

  <svg class="title" viewBox="0 0 750 380" role="img" aria-label="The Harvest Engine of Land">
    <text x="46" y="126" font-size="90" textLength="656" lengthAdjust="spacingAndGlyphs">THE HARVEST ENGINE OF</text>
    <text x="375" y="348" font-size="240" text-anchor="middle" letter-spacing="4">LAND</text>
  </svg>

  <div class="rule rule--top"></div>

  <svg class="edition" viewBox="0 0 750 420" role="img" aria-label="Sydney 2021">
    <text x="374" y="136" text-anchor="middle" font-size="154" textLength="656" lengthAdjust="spacingAndGlyphs">SYDNEY</text>
    <text x="385" y="394" text-anchor="middle" font-size="310" textLength="670" lengthAdjust="spacingAndGlyphs">2021</text>
  </svg>

  <div class="rule rule--bottom"></div>

  <svg class="author" viewBox="0 0 750 140" role="img" aria-label="Colin Marsh, The Housing Ledger Guide">
    <text class="author__name" x="106" y="72" font-size="64" textLength="512" lengthAdjust="spacingAndGlyphs">Colin Marsh</text>
    <text class="author__tag" x="102" y="120" font-size="32" textLength="552" lengthAdjust="spacingAndGlyphs">THE HOUSING LEDGER GUIDE</text>
  </svg>
</main>
</body>
</html>
```